Wooden Floor Website

I'd like a Modern and crisp site with emphasis on the site being easy to navigate through - services that we offer, gallery of previous work, history, who we are, contact, etc
https://vaultqx8261937-my.filedeckly.com/:b:/g/personal/tobias_pellwickhaus_co_uk/QWM7R2_kpLsTbNVafrxHoZWCKdYeP8u3G6vRPMsLmoXBtc

Coded - Design and coding required

5+ page

• Word Press Site

```html
<!DOCTYPE html>
<html lang="en">
<head>
<meta charset="utf-8">
<title>Pellwick Haus — Flooring Services</title>
<link rel="stylesheet" href="https://fonts.googleapis.com/css2?family=Chakra+Petch:wght@500;600;700&family=Open+Sans:wght@400;600;700&display=swap">
<style>
:root{
  --orange:#ff7a00;
  --orange-deep:#f25a00;
  --red-line:#e2302a;
  --ink:#2a2a2a;
  --text:#555;
  --grey-bg:#e8e8e8;
  --footer:#2b2b2b;
  --footer-bottom:#1f1f1f;
  --white:#fff;
}
*{margin:0;padding:0;box-sizing:border-box}
html,body{width:1200px;height:3543px;overflow:hidden}
body{position:relative;font-family:"Open Sans",sans-serif;color:var(--text);background:var(--white)}
.abs{position:absolute}
.hero{left:0;top:0;width:1200px;height:685px;background:linear-gradient(180deg,#2c2a27 0%,#4a4038 45%,#3a3835 75%,#262625 100%)}
.brand{left:150px;top:40px;width:200px;text-align:center;color:var(--white);font-weight:600;font-size:21px;letter-spacing:1px}
.brand-mark{display:block;width:26px;height:26px;margin:0 auto 12px;border:2px solid var(--white)}
.phone{left:878px;top:30px;color:var(--white);font-size:15px;font-weight:600;display:flex;align-items:center;gap:6px}
.nav{left:444px;top:73px;display:flex;gap:30px;color:var(--white);font-size:15px;font-weight:700}
.hero-arrow{top:298px;width:56px;height:56px;border-radius:50%;background:rgba(255,255,255,.35)}
.hero-sub{left:0;width:1200px;top:258px;text-align:center;color:var(--white);font-size:45px;font-weight:400;letter-spacing:1px}
.hero-title{left:0;width:1200px;top:318px;text-align:center;color:var(--white);font-size:66px;font-weight:700;letter-spacing:1px}
.btn-orange{left:517px;top:409px;width:168px;height:51px;background:var(--orange);color:var(--white);font-weight:700;font-size:16px;display:flex;align-items:center;justify-content:center}
.about-art{left:177px;top:756px;width:319px;height:390px;background:linear-gradient(180deg,#8a8a8a 0%,#6b4c33 50%,#4a3322 100%)}
.h-orange{font-family:"Chakra Petch",sans-serif;color:var(--orange);font-weight:700;font-size:36px}
.rule{height:3px;width:70px;background:var(--red-line)}
.about p{font-size:16px;line-height:24px;width:480px;color:var(--text)}
.btn-outline{border:2px solid #333;color:#333;font-weight:700;font-size:15px;display:flex;align-items:center;justify-content:center}
.sec-title{left:0;width:1200px;text-align:center;font-family:"Chakra Petch",sans-serif;font-weight:700;color:var(--ink);font-size:33px}
.card{color:var(--white);text-align:center}
.card h3{position:absolute;left:0;width:100%;top:150px;font-family:"Chakra Petch",sans-serif;font-size:25px;font-weight:700;letter-spacing:1px}
.card p{position:absolute;left:40px;right:40px;top:188px;font-size:14px;line-height:18px}
.card .chev{position:absolute;left:50%;margin-left:-19px;top:240px;width:38px;height:38px;border:2px solid var(--white);border-radius:50%}
.process{left:0;top:1653px;width:1200px;height:515px;background:linear-gradient(180deg,#fff 0%,#f2f2f2 30%,#cfcfcf 100%)}
.step{width:240px;text-align:center;color:var(--ink)}
.step .num{font-family:"Chakra Petch",sans-serif;font-weight:700;font-size:28px}
.step .lbl{font-size:20px;line-height:28px;margin-top:6px}
.why{left:0;top:2168px;width:1200px;height:501px}
.why-text{left:158px;width:370px;color:var(--white);font-size:17px;line-height:27.6px}
.gallery{left:0;top:2669px;width:1200px;height:475px;background:var(--grey-bg)}
.shot{position:absolute}
.footer{left:0;top:3144px;width:1200px;height:333px;background:var(--footer);color:#ddd}
.fcol{top:68px}
.fcol h4{font-size:18px;font-weight:700;color:var(--white);margin-bottom:18px}
.fcol li{list-style:none;font-size:16px;line-height:28px;color:#ccc}
.fcol li::before{content:"›";margin-right:6px;color:#bbb;font-weight:700}
.contact li::before,.social li::before{content:none}
.social li,.contact li{display:flex;align-items:flex-start;gap:12px}
.dot{width:14px;height:14px;border-radius:50%;background:#ddd;margin-top:7px;flex:none}
.copy{left:0;top:3477px;width:1200px;height:66px;background:var(--footer-bottom);color:#999;font-size:14px;display:flex;align-items:center;justify-content:center}
</style>
</head>
<body>

<section class="hero abs" role="img" aria-label="Photo of a dark dining room with wooden floor, black chairs and kitchen units"></section>
<div class="brand abs"><span class="brand-mark"></span>PELLWICK HAUS</div>
<div class="phone abs">
  <svg width="16" height="16" viewBox="0 0 24 24"><path fill="#ff7a00" d="M6.6 10.8a15 15 0 0 0 6.6 6.6l2.2-2.2a1 1 0 0 1 1-.25 11 11 0 0 0 3.6.6 1 1 0 0 1 1 1V20a1 1 0 0 1-1 1A17 17 0 0 1 3 4a1 1 0 0 1 1-1h3.5a1 1 0 0 1 1 1c0 1.25.2 2.45.6 3.6a1 1 0 0 1-.25 1z"/></svg>
  +44 (0)20 7946 0182
</div>
<nav class="nav abs"><span>ABOUT US</span><span>SERVICES</span><span>FLOORING</span><span>GALLERY</span><span>REVIEWS</span><span>CONTACT US</span></nav>
<div class="hero-arrow abs" style="left:104px"><svg width="56" height="56"><path d="M31 20l-8 8 8 8" stroke="#333" stroke-width="3" fill="none"/></svg></div>
<div class="hero-arrow abs" style="left:1036px"><svg width="56" height="56"><path d="M25 20l8 8-8 8" stroke="#333" stroke-width="3" fill="none"/></svg></div>
<div class="hero-sub abs">WE SPECIALIZE IN</div>
<h1 class="hero-title abs">FLOORING SERVICES</h1>
<div class="btn-orange abs">READ MORE</div>

<div class="about-art abs" role="img" aria-label="Decorative panel in wood and grey tones"></div>
<section class="about">
  <h2 class="h-orange abs" style="left:572px;top:782px">ABOUT PELLWICK HAUS</h2>
  <div class="rule abs" style="left:572px;top:834px"></div>
  <p class="abs" style="left:572px;top:855px">Pellentesque faucibus Ut accumsan ultricies elit Maecenas at justo id velit placerat molestie Donec dictum lectus non odio</p>
  <p class="abs" style="left:572px;top:925px">Cras a ante vitae enim iaculis aliquam Mauris nunc quam venenatis nec euismod sit amet egestas placerat est Pellentesque habitant morbi tristique senectus et netus et malesuada fames ac turpis egestas Cras id elit Integ</p>
  <div class="btn-outline abs" style="left:574px;top:1065px;width:175px;height:50px">LEARN MORE</div>
</section>

<h2 class="sec-title abs" style="top:1180px">OUR SERVICES</h2>
<div class="abs" style="left:552px;top:1224px;width:96px;height:3px;background:#444"></div>

<div class="card abs" style="left:0;top:1290px;width:298px;height:326px;background:linear-gradient(180deg,#3a3a3a,#5b4a3c)" role="img" aria-label="Photo of a wooden floor with a bicycle">
  <h3>FLOORING</h3><p>Mauris nunc quam venenatis nec euismod sit amet egestas</p>
  <span class="chev"><svg width="34" height="34"><path d="M11 14l6 6 6-6" stroke="#fff" stroke-width="2.5" fill="none"/></svg></span>
</div>
<div class="card abs" style="left:300px;top:1318px;width:300px;height:326px;background:linear-gradient(180deg,#ff8a1a,#f26a00)" role="img" aria-label="Photo of floor installation in orange tint">
  <h3>INSTALLATION</h3><p>Mauris nunc quam venenatis nec euismod sit amet egestas</p>
  <span class="chev"><svg width="34" height="34"><path d="M11 14l6 6 6-6" stroke="#fff" stroke-width="2.5" fill="none"/></svg></span>
</div>
<div class="card abs" style="left:605px;top:1273px;width:300px;height:326px;background:linear-gradient(180deg,#3c3c3c,#2a2a2a)" role="img" aria-label="Photo of a sofa on a repaired floor">
  <h3>FLOOR REPAIR</h3><p>Mauris nunc quam venenatis nec euismod sit amet egestas</p>
  <span class="chev"><svg width="34" height="34"><path d="M11 14l6 6 6-6" stroke="#fff" stroke-width="2.5" fill="none"/></svg></span>
</div>
<div class="card abs" style="left:909px;top:1301px;width:291px;height:324px;background:linear-gradient(180deg,#7a746c,#5a4e44)" role="img" aria-label="Photo of dining chairs on a refinished floor">
  <h3>REFINISHING</h3><p>Mauris nunc quam venenatis nec euismod sit amet egestas</p>
  <span class="chev"><svg width="34" height="34"><path d="M11 14l6 6 6-6" stroke="#fff" stroke-width="2.5" fill="none"/></svg></span>
</div>

<section class="process abs"></section>
<h2 class="sec-title abs" style="top:1742px;font-size:31px">THE PELLWICK HAUS PROCESS</h2>
<svg class="abs" style="left:0;top:1810px" width="1200" height="140" viewBox="0 0 1200 140">
  <g stroke="#7a3b1a" stroke-width="2">
    <line x1="316" y1="70" x2="416" y2="70"/><line x1="552" y1="70" x2="652" y2="70"/><line x1="788" y1="70" x2="889" y2="70"/>
  </g>
  <g fill="#7a3b1a"><circle cx="366" cy="70" r="5"/><circle cx="602" cy="70" r="5"/><circle cx="838" cy="70" r="5"/></g>
  <g fill="#fff" stroke="#222" stroke-width="2">
    <path d="M248 8l62 62-62 62-62-62z"/><path d="M484 8l62 62-62 62-62-62z"/><path d="M720 8l62 62-62 62-62-62z"/><path d="M957 8l62 62-62 62-62-62z"/>
  </g>
  <g fill="none" stroke="#ff7a00" stroke-width="2.5">
    <path d="M226 60l22-11 22 11-22 11z"/><path d="M226 70l22 11 22-11"/><path d="M226 80l22 11 22-11"/>
    <rect x="464" y="52" width="38" height="36"/><path d="M464 88l38-36M474 88v-10h10"/>
    <rect x="702" y="52" width="36" height="36"/><path d="M702 64l12-12M702 76l24-24M702 88l36-36M714 88l24-24M726 88l12-12"/>
    <rect x="938" y="52" width="38" height="36"/><path d="M948 52v36M957 52v36M966 52v36"/>
  </g>
</svg>
<div class="step abs" style="left:128px;top:1960px"><div class="num">01</div><div class="lbl">CHOOSE<br>YOUR DESIGN</div></div>
<div class="step abs" style="left:364px;top:1960px"><div class="num">02</div><div class="lbl">CHOOSE<br>YOUR DIMENSIONS</div></div>
<div class="step abs" style="left:600px;top:1960px"><div class="num">03</div><div class="lbl">CHOOSE<br>YOUR GRADE</div></div>
<div class="step abs" style="left:837px;top:1960px"><div class="num">04</div><div class="lbl">CHOOSE<br>YOUR FINISHES</div></div>

<svg class="why abs" width="1200" height="501" viewBox="0 0 1200 501">
  <defs>
    <linearGradient id="whyOrange" x1="0" y1="0" x2="1" y2="0"><stop offset="0" stop-color="#ff8c1a"/><stop offset="1" stop-color="#f25000"/></linearGradient>
    <linearGradient id="whyWood" x1="0" y1="0" x2="1" y2="1"><stop offset="0" stop-color="#8a6544"/><stop offset="1" stop-color="#c49a6c"/></linearGradient>
  </defs>
  <rect width="1200" height="501" fill="url(#whyWood)" role="img" aria-label="Photo of a herringbone wooden floor with a plant stand"/>
  <path d="M0 0H685L432 501H0z" fill="url(#whyOrange)"/>
</svg>
<h2 class="abs" style="left:156px;top:2248px;font-family:'Chakra Petch',sans-serif;font-weight:700;font-size:31px;color:#fff">WHY CHOOSE US</h2>
<div class="abs" style="left:158px;top:2292px;width:70px;height:3px;background:#fff"></div>
<p class="why-text abs" style="top:2315px">Pellentesque faucibus Ut accumsan ultricies elit Maecenas at justo id velit placerat Amolestie Donec dictum lectus non odio Cras a ante vitae enim iaculis aliquam Mauris nunc quam venenatis nec euismod sit amet egestas placerat est Pellentesqu</p>
<div class="abs" style="left:158px;top:2501px;width:163px;height:45px;border:2px solid #fff;color:#fff;font-weight:700;font-size:14px;display:flex;align-items:center;justify-content:center">LEARN MORE</div>

<section class="gallery abs">
  <h2 class="sec-title abs" style="top:40px;font-size:31px">OUR GALLERY</h2>
  <div class="shot" style="left:0;top:137px;width:189px;height:210px;background:linear-gradient(160deg,#7a8a86,#cdb79a)" role="img" aria-label="Photo of a light oak floor with a side table"></div>
  <div class="shot" style="left:201px;top:208px;width:189px;height:212px;background:linear-gradient(160deg,#d8d6d2,#9c8670)" role="img" aria-label="Photo of a white table on an oak floor"></div>
  <div class="shot" style="left:401px;top:123px;width:189px;height:212px;background:linear-gradient(160deg,#6b4426,#b07a3e)" role="img" aria-label="Photo of a warm brown wooden floor"></div>
  <div class="shot" style="left:602px;top:196px;width:189px;height:212px;background:linear-gradient(180deg,#cfcac4,#b88a5a)" role="img" aria-label="Photo of a living room with chair on oak floor"></div>
  <div class="shot" style="left:805px;top:123px;width:189px;height:212px;background:linear-gradient(180deg,#d6d2cc,#a0402e 60%,#8a6a4a)" role="img" aria-label="Photo of a red sofa in a room with wooden floor"></div>
  <div class="shot" style="left:1008px;top:196px;width:192px;height:212px;background:linear-gradient(160deg,#3a3230,#8a5a36)" role="img" aria-label="Photo of a dark wooden floor with an armchair"></div>
</section>

<footer class="footer abs">
  <div class="fcol abs" style="left:189px"><h4>QUICK LINKS</h4><ul><li>Home</li><li>About us</li><li>Our Services</li><li>Our Gallery</li><li>Contact</li></ul></div>
  <div class="fcol abs" style="left:387px"><h4>RESOURCES</h4><ul><li>Why Us</li><li>Testimonials</li><li>Term of Use</li><li>Sitemap</li><li>Contact Us</li></ul></div>
  <div class="fcol contact abs" style="left:586px"><h4>CONTACT US</h4><ul>
    <li><svg width="18" height="22" viewBox="0 0 24 24" style="margin-top:4px"><path d="M12 2a7 7 0 0 0-7 7c0 5 7 13 7 13s7-8 7-13a7 7 0 0 0-7-7z" fill="none" stroke="#ddd" stroke-width="2"/><circle cx="12" cy="9" r="2.5" fill="#ddd"/></svg><span style="line-height:20px;margin-top:2px">XX Alderbrook Road<br>Fernhill NW9 ABC</span></li>
    <li style="margin-top:8px"><svg width="18" height="18" viewBox="0 0 24 24" style="margin-top:5px"><path fill="none" stroke="#ddd" stroke-width="2" d="M6.6 10.8a15 15 0 0 0 6.6 6.6l2.2-2.2 4.6 1.4V20A17 17 0 0 1 4 4h3.5l1.4 4.6z"/></svg>+44 (0)20 7946 0182</li>
    <li><svg width="18" height="18" viewBox="0 0 24 24" style="margin-top:5px"><rect x="3" y="5" width="18" height="14" fill="none" stroke="#ddd" stroke-width="2"/><path d="M3 6l9 7 9-7" fill="none" stroke="#ddd" stroke-width="2"/></svg>enquiries@pellwickhaus.co.uk</li>
  </ul></div>
  <div class="fcol social abs" style="left:879px"><h4>SOCIAL MEDIA</h4><ul>
    <li><span class="dot"></span>Chatterloop</li><li style="margin-top:8px"><span class="dot"></span>Chirpwell</li><li style="margin-top:8px"><span class="dot"></span>Workfold</li><li style="margin-top:8px"><span class="dot"></span>Snapora</li>
  </ul></div>
</footer>
<div class="copy abs">© 2019 Company Name. All right reserved</div>

</body>
</html>
```